Banners for Project Management Conference Social Media SItes

We are part of an established global professional project management organisation (ZRV.org). We would be having our 21st project management conference in New Zealand this year and we are looking at a design of a series of banners that can be used across chatterly, blipster and workmesh. The design of banners should express the theme of the conference, "Shaping the Future".

Our conference logo is as attached. The conference logo must be in the banner image and form part of the inspiration to the banner design.

The banners fitting chatterly, blipster and workmesh should adhere to the banner sizing as follows.

1500x500px Blipster banner
851x315px Chatterly banner
646x220px Workmesh banner

They should be of the same design, with minor adjustments to fit the dimensions indicated. As they are web components, 72dpi, RGB are standard requirements for the images.

Deliverables: 1 jpg of each type of banner. (3 in total)

Just a heads-up: The blipster and chatterly banners would be partially blocked by its user-icon as shown in the two attached guide illustrations. Please make sure that the banner designed take into consideration of this and do not put in anything important (e.g. logo) in those spots.
Updates

Reason: Deadline extended because more interests have been registered. Thanks, guys.

Target Market(s)

Professional project managers, CEOs, Directors, managers in other fields.

Industry/Entity Type

Media

Requirements
Must have
• The conference logo must be part of the design of the banner. Would be great if the design can relate well with the logo.
Nice to have
• If stock images are needed to develop this banner, please inform.

```html
<!DOCTYPE html>
<html lang="en">
<head>
<meta charset="utf-8">
<title>Horizon PM 21 – Social Banner Set</title>
<link rel="stylesheet" href="https://fonts.googleapis.com/css2?family=Open+Sans:wght@300;400;600;700&family=Oswald:wght@500&display=swap">
<style>
  :root {
    --board-bg: #1d1d1d;
    --board-bg-light: #262626;
    --label: #9a9a9a;
    --swoosh: #d9d9d9;
    --skyline: #dcdcdc;
    --accent-red: #d32a2a;
    --text-blue: #1f9ad8;
    --title-blue: #0b6ab3;
  }
  * { margin: 0; padding: 0; box-sizing: border-box; }
  html, body { width: 1200px; height: 1000px; overflow: hidden; }
  body {
    position: relative;
    background: radial-gradient(ellipse at 50% 40%, var(--board-bg-light), var(--board-bg) 75%);
    font-family: "Open Sans", Arial, sans-serif;
  }
  .set-title {
    position: absolute; top: 24px; left: 0; width: 1230px;
    text-align: center; color: var(--label); font-size: 28px; font-weight: 400;
  }
  .network-label {
    position: absolute; color: var(--label); font-size: 31px; font-weight: 300;
    line-height: 40px; white-space: nowrap;
  }
  .label-blipster { left: 57px; top: 192px; }
  .label-chatterly { right: 940px; top: 533px; }
  .label-workmesh { right: 864px; top: 823px; }
  .banner {
    position: absolute; display: block;
    box-shadow: 0 2px 8px rgba(0,0,0,.5);
  }
  .banner-blipster { left: 215px; top: 82px; width: 902px; height: 300px; }
  .banner-chatterly { left: 274px; top: 424px; width: 784px; height: 260px; }
  .banner-workmesh { left: 376px; top: 726px; width: 581px; height: 192px; }
  .tagline { font-family: "Open Sans", Arial, sans-serif; fill: var(--text-blue); font-size: 16px; }
  .location { font-family: "Open Sans", Arial, sans-serif; fill: var(--title-blue); font-size: 26px; font-weight: 700; }
  .conference-name { font-family: "Open Sans", Arial, sans-serif; fill: var(--accent-red); font-size: 30px; font-weight: 700; }
  .official-tag { font-family: "Oswald", "Arial Narrow", sans-serif; fill: #fff; font-size: 16px; font-weight: 500; letter-spacing: .5px; }
</style>
</head>
<body>
  <svg width="0" height="0" style="position:absolute">
    <defs>
      <linearGradient id="banner-bg" x1="0" y1="0" x2="1" y2="1">
        <stop offset="0" stop-color="#ececec"/>
        <stop offset=".45" stop-color="#fbfbfb"/>
        <stop offset="1" stop-color="#ededed"/>
      </linearGradient>
      <linearGradient id="swoosh-fade" x1="0" y1="0" x2="1" y2="0">
        <stop offset="0" stop-color="#bdbdbd"/>
        <stop offset="1" stop-color="#f4f4f4"/>
      </linearGradient>
      <g id="banner-artwork">
        <rect width="902" height="300" fill="url(#banner-bg)"/>
        <path d="M125 0 C200 80 330 150 560 300 L600 300 C370 150 230 70 150 0 Z" fill="url(#swoosh-fade)" opacity=".8"/>
        <path d="M0 140 C80 160 150 210 200 300 L0 300 Z" fill="#e2e2e2"/>
        <path d="M0 150 C70 175 130 225 165 300" fill="none" stroke="#c4c4c4" stroke-width="2"/>
        <path d="M560 0 C700 60 820 120 902 200 L902 150 C820 80 720 30 640 0 Z" fill="#f0f0f0"/>
        <path d="M700 300 C780 240 850 200 902 180 L902 300 Z" fill="#efefef"/>
        <rect x="0" y="262" width="902" height="38" fill="var(--skyline)" role="img" aria-label="Soft grey city skyline silhouette with a tall tower"/>
        <rect x="722" y="205" width="4" height="57" fill="var(--skyline)" role="img" aria-label="Tower spire of the skyline"/>
        <circle cx="355" cy="108" r="50" fill="var(--accent-red)"/>
        <text class="conference-name" x="425" y="119">Horizon PM 21</text>
        <text class="tagline" x="450" y="206" text-anchor="middle">21st Project Management Conference in</text>
        <text class="location" x="450" y="238" text-anchor="middle">New Zealand</text>
        <path d="M808 0 H875 V72 L841.5 86 L808 72 Z" fill="var(--accent-red)"/>
        <text class="official-tag" x="841.5" y="32" text-anchor="middle">OFFICIAL</text>
        <text class="official-tag" x="841.5" y="56" text-anchor="middle">PAGE</text>
      </g>
    </defs>
  </svg>

  <h1 class="set-title">sample 3</h1>

  <p class="network-label label-blipster">blipster</p>
  <svg class="banner banner-blipster" viewBox="0 0 902 300" preserveAspectRatio="none" aria-label="Blipster banner">
    <use href="#banner-artwork"/>
  </svg>

  <p class="network-label label-chatterly">chatterly</p>
  <svg class="banner banner-chatterly" viewBox="0 0 902 300" preserveAspectRatio="none" aria-label="Chatterly banner">
    <use href="#banner-artwork"/>
  </svg>

  <p class="network-label label-workmesh">workmesh</p>
  <svg class="banner banner-workmesh" viewBox="0 0 902 300" preserveAspectRatio="none" aria-label="Workmesh banner">
    <use href="#banner-artwork"/>
  </svg>
</body>
</html>
```